Business Card Design Project

Hello,

We have just created our new COMPANY LOGO via Pixel Harbor and would not like to turn our attention to new Business Cards.

We are a printing company based in Singapore & Las Vegas. We specialize in blue-print printing for the Architectural, Engineering and Construction industries

The design should be simple, professional, clean and organized.

The Business Cards should "pop" when seen and will hopefully be something that makes you look twice.

We have two different Pan-tones that we use for our company, feel free to use them if you think they will work for your design?

Orange: PMS 021
Gray: PMS 431

I have attached our current logo for your use and reference which should obvious be on our business cards.

Considering we have two locations on different continents, we need business cards templates where the address details need to be interchangeable for each different location (total 2)

First one:
38 Merrow Lane #03-11 to #03-15
Singapore 528473
Tel : +65 6847-3920
Fax : +65 6843-7702

Second one:
2381 W. Tanfield Rd, Suite 204
Las Vegas, Nevada 89152
Tel : (702) 555-4137
Fax : (702) 555-4189

We would also like to list a few of our key services on the card. Here are a few examples to get you going.

Plan Printing & Plotting
Digital Colour Printing
Cadline Printing
Specialty Book Making
Scanning & Archiving
Collection & Delivey

This is the first time i have requested for business cards to be created so please let me know if you require any additional information.
Many Thanks,
Tobin
Updates

Project Deadline Extended
Reason: It took us longer than expected to finalize our Company Logo We look forward to receiving your designs.

Target Market(s)

Our Target Market is construction related people.
Construction
Architecture
Engineering

Industry/Entity Type

Printing

Font styles to use
Other font styles liked:
• Times New Roman

Colors
faa54b
ffffff

Requirements
Must have
• The business card must have our Company Logo (attached)
The font used must be Times New Roman
Should not have
• Playful images of print designs and/or logos

```html
<!DOCTYPE html>
<html lang="en">
<head>
<meta charset="utf-8">
<title>Linecraft Print Works – Business Card</title>
<link rel="stylesheet" href="https://fonts.googleapis.com/css2?family=Tinos:ital,wght@0,400;0,700;1,700&display=swap">
<style>
  :root {
    --orange: #faa54b;
    --white: #ffffff;
    --ink: #111111;
    --card-edge: #b9b9bb;
    --stage-light: #e6e6e7;
    --stage-dark: #c4c4c7;
  }
  * { margin: 0; padding: 0; box-sizing: border-box; }
  html, body { width: 1200px; height: 1000px; overflow: hidden; }
  body {
    position: relative;
    font-family: "Tinos", "Times New Roman", serif;
    color: var(--ink);
    background: radial-gradient(ellipse 620px 520px at 600px 500px, var(--stage-light), var(--stage-dark));
  }
  .option-label {
    position: absolute; left: 30px; top: 42px;
    font-size: 25px; line-height: 1;
  }
  .card {
    position: absolute; left: 110px; top: 230px;
    width: 980px; height: 540px;
    background: var(--white);
    border: 1px solid var(--card-edge);
    overflow: hidden;
  }
  .band-top { position: absolute; left: 0; top: 0; width: 100%; height: 31px; background: var(--orange); }
  .band-bottom { position: absolute; left: 0; bottom: 0; width: 100%; height: 17px; background: var(--orange); }
  .swoosh { position: absolute; left: 0; top: 352px; width: 980px; height: 80px; }
  .brand {
    position: absolute; left: 48px; top: 150px; width: 420px;
    text-align: center;
  }
  .brand-name { font-size: 40px; font-weight: 700; line-height: 1.1; }
  .brand-tagline { margin-top: 8px; font-size: 20px; font-weight: 700; font-style: italic; }
  .contact {
    position: absolute; right: 38px; top: 54px;
    text-align: right; font-style: normal; font-weight: 700;
    font-size: 40px; line-height: 54px;
  }
  .services { list-style: none; }
  .services li {
    position: absolute; white-space: nowrap;
    font-size: 29px; line-height: 32px;
  }
  .row-1 { top: 432px; }
  .row-2 { top: 469px; }
  .plan { left: 66px; }
  .digital { left: 407px; }
  .cadline { left: 748px; }
  .book { left: 55px; }
  .scanning { left: 396px; }
  .delivery { left: 699px; }
</style>
</head>
<body>
  <div class="option-label">Option_2_1</div>

  <section class="card">
    <div class="band-top"></div>

    <div class="brand">
      <div class="brand-name">Linecraft Print Works</div>
      <div class="brand-tagline">A Member of the Linecraft Group of Companies</div>
    </div>

    <address class="contact">
      <div>38 Merrow Lane</div>
      <div>#03-11 to #03-15</div>
      <div>Singapore 528473</div>
      <div>Tel : +65 6847-3920</div>
      <div>Fax : +65 6843-7702</div>
    </address>

    <svg class="swoosh" viewBox="0 0 980 80" aria-hidden="true">
      <path d="M0 4 Q490 126 980 4 Q490 82 0 4 Z" fill="var(--orange)"/>
    </svg>

    <ul class="services">
      <li class="row-1 plan">Plan Printing &amp; Plotting</li>
      <li class="row-1 digital">Digital Colour Printing</li>
      <li class="row-1 cadline">Cadline Printing</li>
      <li class="row-2 book">Specialty Book Making</li>
      <li class="row-2 scanning">Scanning &amp; Archiving</li>
      <li class="row-2 delivery">Collection &amp; Delivey</li>
    </ul>

    <div class="band-bottom"></div>
  </section>
</body>
</html>
```